Business Card for Brenwick Painting

We need a simple, yet out standing business card for our painting company.

Target Market(s)

wealthy; high-end neighborhoods, and businesses

Industry/Entity Type

Painting

Contact Information for Business Card

Name:
Dorian Vask

Email:
d.vask@brenwick-painting.example

Website:
Brenwick-painting.example

Phone Number:
(555) 412-9063

Font styles to use
Serif
Sans Serif

Requirements
Must have
• slogan "Color Made Effortless"
Should not have
• A title attached to the name on the card

```html
<!DOCTYPE html>
<html lang="en">
<head>
<meta charset="utf-8">
<title>Brenwick Painting – Business Card</title>
<link rel="stylesheet" href="https://fonts.googleapis.com/css2?family=Crimson+Pro:wght@500;700&family=Arimo:wght@400&display=swap">
<style>
  :root {
    --page: #ffffff;
    --green-bright: #66e31c;
    --green-light: #86f02e;
    --green-deep: #4fc812;
    --olive: #3a4912;
    --olive-text: #3d4a14;
    --band: #7ef22a;
    --rule: #9cf55a;
    --white: #ffffff;
    --serif: "Crimson Pro", Georgia, serif;
    --sans: "Arimo", Arial, sans-serif;
  }
  * { margin: 0; padding: 0; box-sizing: border-box; }
  html, body {
    width: 998px; height: 1200px; overflow: hidden;
    background: var(--page);
  }
  .canvas { position: relative; width: 998px; height: 1200px; }

  .card {
    position: absolute;
    width: 875px; height: 512px;
    overflow: hidden;
    background:
      radial-gradient(ellipse 40% 30% at 30% 30%, var(--green-light), transparent 70%),
      radial-gradient(ellipse 35% 28% at 75% 70%, var(--green-light), transparent 70%),
      radial-gradient(ellipse 50% 40% at 55% 95%, var(--green-deep), transparent 70%),
      var(--green-bright);
  }
  .card--front { left: 66px; top: 62px; }
  .card--back  { left: 63px; top: 624px; }

  /* Front */
  .front-name {
    position: absolute; left: 0; right: 0; top: 232px;
    text-align: center;
    font-family: var(--serif); font-weight: 500;
    font-size: 54px; letter-spacing: 3px;
    color: var(--olive-text);
    text-transform: uppercase;
  }
  .slogan-band {
    position: absolute; left: 0; right: 0; top: 341px; height: 50px;
    background: var(--band);
    border-top: 2px solid var(--rule);
    border-bottom: 2px solid var(--rule);
  }
  .slogan {
    position: absolute; left: 0; right: 0; top: 0;
    line-height: 46px;
    text-align: center;
    font-family: var(--serif); font-weight: 700;
    font-size: 38px; letter-spacing: 2px;
    color: var(--olive-text);
    text-transform: uppercase;
  }

  /* Back */
  .brand-panel {
    position: absolute; left: 470px; top: 0; right: 0; bottom: 0;
    background: var(--olive);
  }
  .person-name {
    position: absolute; left: 30px; top: 62px;
    font-family: var(--serif); font-weight: 700;
    font-size: 38px; letter-spacing: 1px;
    color: var(--white);
    text-transform: uppercase;
  }
  .name-rule {
    position: absolute; left: 30px; top: 105px; width: 825px; height: 2px;
    background: var(--rule);
    z-index: 2;
  }
  .contact {
    position: absolute; left: 30px; top: 118px;
    list-style: none;
    font-family: var(--sans); font-size: 21px;
    color: var(--white);
  }
  .contact li { display: flex; align-items: center; height: 33px; }
  .contact svg { width: 18px; height: 18px; margin-right: 8px; flex: none; }

  .panel-name {
    position: absolute; left: 36px; right: 16px; top: 355px;
    font-family: var(--serif); font-weight: 500;
    font-size: 33px; letter-spacing: 2px;
    color: var(--white);
    text-transform: uppercase;
  }
  .panel-rule {
    position: absolute; left: 36px; top: 432px; width: 336px; height: 2px;
    background: var(--rule);
  }
  .website {
    position: absolute; left: 36px; top: 445px;
    font-family: var(--sans); font-size: 23px; letter-spacing: 1.5px;
    color: var(--white);
  }
</style>
</head>
<body>
<div class="canvas">

  <section class="card card--front" aria-label="Card front">
    <div class="front-name">Brenwick Painting</div>
    <div class="slogan-band">
      <p class="slogan">Color Made Effortless</p>
    </div>
  </section>

  <section class="card card--back" aria-label="Card back">
    <div class="brand-panel">
      <div class="panel-name">Brenwick Painting</div>
      <div class="panel-rule"></div>
      <p class="website">Brenwick-painting.example</p>
    </div>

    <h1 class="person-name">Dorian Vask</h1>
    <div class="name-rule"></div>
    <ul class="contact">
      <li>
        <svg viewBox="0 0 18 18" aria-hidden="true">
          <rect x="0.5" y="0.5" width="17" height="17" rx="2" fill="#a6f56a"/>
          <rect x="3.5" y="5" width="11" height="8" fill="none" stroke="#4fb816" stroke-width="1.2"/>
          <path d="M3.5 5 L9 9.5 L14.5 5" fill="none" stroke="#4fb816" stroke-width="1.2"/>
        </svg>
        d.vask@brenwick-painting.example
      </li>
      <li>
        <svg viewBox="0 0 18 18" aria-hidden="true">
          <rect x="0.5" y="0.5" width="17" height="17" rx="2" fill="#a6f56a"/>
          <path d="M6 4 L8 4 L8.5 7 L7.3 8 Q8.5 10.5 10 11 L11 9.8 L14 10.3 L14 12.5 Q10 14 6.5 10 Q4.5 7 6 4 Z" fill="#4fb816"/>
        </svg>
        (555) 412-9063
      </li>
    </ul>
  </section>

</div>
</body>
</html>
```